Local Roofing/Construction company business needs new biz card design

We need a new business card design, current cards are from the start of this operation and generic at best. We are a local Construction Company (General Contractor) with a majority of our work originating from insurance claims-exterior finish work is the main focus (Roofs-Siding-Gutters etc). Heavily involved with homeowners and the low ball offers they receive from insurance company's after a insurable event takes place. I have attached some of our original logo file(s) below.

```html
<!DOCTYPE html>
<html lang="en">
<head>
<meta charset="utf-8">
<title>Stonebrook Construction – Business Card</title>
<link rel="stylesheet" href="https://fonts.googleapis.com/css2?family=Open+Sans:wght@400;600;700&display=swap">
<style>
  :root {
    --stage: #232323;
    --card-dark: #061d22;
    --card-dark-edge: #0a262c;
    --card-dark-deep: #040f12;
    --green: #4fbf6b;
    --green-deep: #2f9a4c;
    --green-soft: #7fd494;
    --text-light: #e8ecec;
    --text-dark: #0a2328;
  }
  * { box-sizing: border-box; margin: 0; padding: 0; }
  html, body {
    width: 1200px; height: 780px; overflow: hidden;
    background: var(--stage);
    font-family: "Open Sans", Arial, sans-serif;
  }
  .canvas {
    position: relative; width: 1200px; height: 780px;
    display: flex; align-items: center; justify-content: center; gap: 40px;
  }
  .card {
    position: relative; width: 540px; height: 310px;
    border-radius: 4px; overflow: hidden;
    box-shadow: 0 18px 40px rgba(0,0,0,.45);
  }

  /* Front */
  .card--front { background: var(--card-dark); color: var(--text-light); }
  .front-shade {
    position: absolute; left: 250px; bottom: 0; width: 200px; height: 62px;
    background: linear-gradient(135deg, var(--card-dark-edge), var(--card-dark-deep) 70%);
    opacity: .8; z-index: 0;
  }
  .brand, .contact, .person, .edge-tab { z-index: 1; }
  .brand {
    position: absolute; left: 34px; top: 32px;
    display: flex; align-items: center; gap: 12px;
  }
  .brand__mark { width: 22px; height: 22px; background: var(--green); }
  .brand__name {
    font-weight: 700; font-size: 24px; letter-spacing: .5px;
    text-transform: uppercase; color: var(--green); line-height: 1;
  }
  .contact {
    position: absolute; left: 34px; top: 104px;
    font-size: 13px; line-height: 1.55;
  }
  .contact__address { margin-bottom: 6px; }
  .contact__row { display: flex; align-items: center; gap: 8px; }
  .contact__row svg { width: 12px; height: 12px; flex: none; }
  .person {
    position: absolute; right: 36px; top: 150px; text-align: right;
  }
  .person__name {
    font-weight: 700; font-size: 30px; color: var(--green); line-height: 1.1;
  }
  .person__role { font-size: 17px; color: var(--text-light); margin-top: 2px; }
  .edge-tab {
    position: absolute; right: 0; top: 168px; width: 12px; height: 64px;
    background: var(--green);
  }

  /* Back */
  .card--back { background: var(--green); }
  .back-pattern {
    position: absolute; inset: 0;
    background: linear-gradient(120deg, var(--green-deep) 0%, var(--green) 55%, var(--green-soft) 100%);
    opacity: .55;
  }
  .back-brand {
    position: absolute; right: 44px; bottom: 60px;
    display: flex; align-items: center; gap: 8px;
  }
  .back-brand__mark { width: 14px; height: 14px; background: var(--text-dark); }
  .back-brand__name {
    font-weight: 700; font-size: 15px; text-transform: uppercase;
    letter-spacing: .4px; color: var(--text-dark);
  }
</style>
</head>
<body>
<main class="canvas">

  <section class="card card--front" aria-label="Business card front">
    <div class="front-shade" role="img" aria-label="Large tonal brand emblem decoration"></div>

    <div class="brand">
      <span class="brand__mark"></span>
      <span class="brand__name">Stonebrook Construction</span>
    </div>

    <div class="contact">
      <p class="contact__address">42 Oak Hollow Ln<br>Fairview, MO 63010</p>
      <p class="contact__row">
        <svg viewBox="0 0 12 12" aria-hidden="true"><path fill="var(--green)" d="M2.5 1l2 2.2-1 1.2a6 6 0 0 0 4 4l1.2-1 2.3 2-1.3 1.6C5 11 1 7 .9 2.3z"/></svg>
        555-014-2280
      </p>
      <p class="contact__row">
        <svg viewBox="0 0 12 12" aria-hidden="true"><path fill="var(--green)" d="M2.5 1l2 2.2-1 1.2a6 6 0 0 0 4 4l1.2-1 2.3 2-1.3 1.6C5 11 1 7 .9 2.3z"/></svg>
        555-017-3391 (Emergency)
      </p>
      <p class="contact__row">
        <svg viewBox="0 0 12 12" aria-hidden="true"><circle cx="6" cy="6" r="5" fill="none" stroke="var(--green)" stroke-width="1.3"/><path d="M1 6h10M6 1c-2.5 3-2.5 7 0 10M6 1c2.5 3 2.5 7 0 10" fill="none" stroke="var(--green)" stroke-width="1"/></svg>
        www.stonebrookbuild.com
      </p>
      <p class="contact__row">
        <svg viewBox="0 0 12 12" aria-hidden="true"><rect x=".8" y="2.5" width="10.4" height="7" fill="none" stroke="var(--green)" stroke-width="1.2"/><path d="M1 3l5 3.6L11 3" fill="none" stroke="var(--green)" stroke-width="1.2"/></svg>
        hello@stonebrookbuild.com
      </p>
    </div>

    <div class="person">
      <p class="person__name">Marta Delane</p>
      <p class="person__role">Co-Founder</p>
    </div>
    <span class="edge-tab"></span>
  </section>

  <section class="card card--back" aria-label="Business card back">
    <div class="back-pattern" role="img" aria-label="Repeating brand emblem pattern fading toward lighter green"></div>
    <div class="back-brand">
      <span class="back-brand__mark"></span>
      <span class="back-brand__name">Stonebrook Construction</span>
    </div>
  </section>

</main>
</body>
</html>
```